business card for a massage therapy practice named 'Meadow and Rowan Massage Studio'

I really need a trendy, yet easy on the eyes business card to complement my logo. Ideally with some gold or rose gold foil work.

My uploaded file of the logo I have in horizontal but I have a vertical version as well. Another color that is used in the website is a blush pink here and there. I'd like to see some trendy tropical leaves in the design.

```html
<!DOCTYPE html>
<html lang="en">
<head>
<meta charset="utf-8">
<title>Meadow and Rowan Massage Studio – Business Card</title>
<link href="https://fonts.googleapis.com/css2?family=Open+Sans:wght@400;600&display=swap" rel="stylesheet">
<style>
  :root {
    --backdrop: #2f3032;
    --card-white: #ffffff;
    --card-dark: #4b4b4e;
    --card-dark-deep: #3a3a3c;
    --ink: #2a2a2a;
    --teal: #5fcfb1;
    --gold: #b59f6e;
    --gold-light: #cdb98a;
    --photo-skin: #d9b8a6;
    --photo-sweater: #a8a8aa;
  }
  * { box-sizing: border-box; margin: 0; padding: 0; }
  html, body { width: 1200px; height: 782px; overflow: hidden; }
  body {
    background: var(--backdrop);
    font-family: "Open Sans", Arial, sans-serif;
    color: var(--ink);
    display: flex;
    align-items: center;
    justify-content: center;
    gap: 40px;
  }
  .card {
    width: 540px;
    height: 309px;
    position: relative;
    overflow: hidden;
    box-shadow: 0 10px 28px rgba(0,0,0,.45);
  }

  /* Front */
  .card-front {
    background: var(--card-white);
    border-bottom: 8px solid var(--gold);
  }
  .brand {
    position: absolute;
    left: 150px;
    top: 48px;
    display: flex;
    align-items: center;
    gap: 16px;
  }
  .brand-mark {
    width: 46px; height: 46px;
    border-radius: 50%;
    background: var(--gold);
    flex: none;
  }
  .brand-name {
    font-weight: 600;
    font-size: 25px;
    line-height: 1.15;
    color: var(--ink);
  }
  .brand-name span { display: block; font-size: 15px; letter-spacing: 3px; text-transform: uppercase; }
  .therapist {
    position: absolute;
    left: 30px;
    top: 150px;
  }
  .therapist-name {
    color: var(--teal);
    font-size: 17px;
    letter-spacing: .5px;
    text-transform: uppercase;
  }
  .therapist-license { font-size: 12px; margin-top: 2px; }
  .contact-list {
    list-style: none;
    margin-top: 6px;
    font-size: 14px;
    line-height: 1.4;
  }
  .contact-list li { display: flex; align-items: center; gap: 7px; }
  .contact-list svg { width: 11px; height: 11px; fill: var(--teal); flex: none; }
  .address {
    position: absolute;
    right: 30px;
    bottom: 22px;
    text-align: right;
    font-size: 15px;
    line-height: 1.35;
  }

  /* Back */
  .card-back {
    background: linear-gradient(180deg, var(--card-dark) 0%, var(--card-dark-deep) 100%);
    color: #fff;
  }
  .services {
    position: absolute;
    left: 32px;
    top: 48px;
    list-style: none;
    font-size: 13.5px;
    line-height: 1.5;
    text-transform: uppercase;
    letter-spacing: .3px;
    z-index: 1;
  }
  .services li::before {
    content: "";
    display: inline-block;
    width: 6px; height: 6px;
    border-radius: 50%;
    background: var(--teal);
    margin-right: 7px;
    vertical-align: middle;
  }
  .social {
    position: absolute;
    left: 32px;
    top: 150px;
    display: flex;
    align-items: center;
    gap: 8px;
    font-size: 13px;
    z-index: 1;
  }
  .social-dot { width: 14px; height: 14px; border-radius: 50%; background: #fff; }
  .photo {
    position: absolute;
    right: 0; bottom: 0;
    width: 300px; height: 220px;
    background:
      radial-gradient(ellipse at 75% 40%, var(--photo-skin) 0%, rgba(217,184,166,.7) 35%, transparent 65%),
      linear-gradient(160deg, transparent 20%, var(--photo-sweater) 70%);
  }
</style>
</head>
<body>
  <section class="card card-front">
    <div class="brand">
      <div class="brand-mark"></div>
      <div class="brand-name">Meadow &amp; Rowan<span>Massage Studio</span></div>
    </div>
    <div class="therapist">
      <p class="therapist-name">Elena Marsh</p>
      <p class="therapist-license">LMT #40218</p>
      <ul class="contact-list">
        <li><svg viewBox="0 0 12 12"><path d="M3 1h2l1 3-1.5 1a7 7 0 0 0 2.5 2.5L8 6l3 1v2a2 2 0 0 1-2 2A9 9 0 0 1 1 3a2 2 0 0 1 2-2z"/></svg>(555) 014-2290</li>
        <li><svg viewBox="0 0 12 12"><path d="M1 2h10v8H1z M1 2l5 4 5-4" stroke="#fff" stroke-width=".8"/></svg>meadowandrowan@mail.com</li>
        <li><svg viewBox="0 0 12 12"><circle cx="6" cy="6" r="5.5"/></svg>www.meadowandrowan.com</li>
      </ul>
    </div>
    <p class="address">418 Linden Ave. suite 210<br>Riverton, CA 95020</p>
  </section>

  <section class="card card-back">
    <ul class="services">
      <li>Pain Management</li>
      <li>Anxiety and Depression Support</li>
      <li>Lymphatic Drainage Massage</li>
    </ul>
    <div class="social"><span class="social-dot"></span>@meadowandrowan</div>
    <div class="photo" role="img" aria-label="Photo of a therapist's hands massaging a client's neck and shoulders"></div>
  </section>
</body>
</html>
```